Energy Company 8-page Brochure

We are in need of a redesign of our 8-page brochure. Attached is the initial design that does not represent us very well. We are looking for CLEAN/CORPORATE look with a little bit of flair (graphs/charts if applicable).

I prefer white background and our company colors (blue/green) to be the accent colors. Feel free to add additional accent colors to highlight certain areas.

We are in the energy field (not just solar), so please consider the types of images that you will use. Are headquarters is located in Chicago, IL so a great looking picture of the skyline or something similar would work for the front and back cover.

We have additional marketing collateral that we will want to be uniformed once we have the right design.

Good luck, and we look forward to receiving some great designs!

Best Regards,
Kurt

Target Market(s)

Small to large businesses (B2B).

Industry/Entity Type

It Company

Colors
ffffff
9bcb3c
0255a3

Requirements
Must have
• Clean design, company colors, specified content and editable files.
Nice to have
• Graphs, charts, highlighted areas where necessary.
Should not have
• Clutter! Please utilized page space appropriately. There is a lot of content, so you need to consider graphics and image placement.

```html
<!DOCTYPE html>
<html lang="en">
<head>
<meta charset="utf-8">
<title>Success Stories – Brochure Spread</title>
<link rel="stylesheet" href="https://fonts.googleapis.com/css2?family=Source+Sans+3:wght@300;400;600;700&display=swap">
<style>
  :root {
    --bg: #646b72;
    --paper: #ffffff;
    --blue: #0255a3;
    --green: #6aa236;
    --green-bright: #9bcb3c;
    --grey-text: #7a7a7a;
    --rule: #9a9a9a;
    --ring-base: #b5b5b5;
  }
  * { margin: 0; padding: 0; box-sizing: border-box; }
  html, body { width: 1200px; height: 862px; overflow: hidden; }
  body { background: var(--bg); font-family: "Source Sans 3", Arial, sans-serif; position: relative; }

  .spread { position: absolute; left: 52px; top: 67px; width: 1098px; height: 713px; background: var(--paper); overflow: hidden; }
  .page { position: absolute; top: 0; width: 549px; height: 713px; }
  .page--left { left: 0; }
  .page--right { left: 549px; }
  .spine { position: absolute; left: 520px; top: 0; width: 60px; height: 713px;
    background: linear-gradient(90deg, rgba(0,0,0,0) 0%, rgba(0,0,0,0.05) 45%, rgba(0,0,0,0.08) 50%, rgba(0,0,0,0.02) 55%, rgba(0,0,0,0) 100%); }

  .rule { position: absolute; height: 2px; background: var(--rule); }

  /* Left page */
  .kicker { position: absolute; left: 60px; top: 59px; font-size: 15px; color: var(--blue); }
  .page-title { position: absolute; left: 59px; top: 68px; font-size: 41px; font-weight: 600; color: var(--green); letter-spacing: 0.3px; }

  .stat { position: absolute; width: 180px; }
  .stat__figure { display: flex; align-items: center; gap: 8px; height: 50px; }
  .stat__value { font-size: 48px; font-weight: 400; line-height: 1; }
  .stat__value--blue { color: var(--blue); }
  .stat__value--green { color: var(--green); }
  .stat__text { margin-top: 12px; font-size: 12.5px; line-height: 14px; color: var(--grey-text); }
  .stat__lead { text-transform: uppercase; }
  .stat__lead--blue { color: var(--blue); }
  .stat__lead--green { color: var(--green); }
  .donut { width: 46px; height: 46px; flex: none; }

  .brand { position: absolute; top: 644px; display: flex; align-items: center; gap: 6px; font-size: 13px; font-weight: 600; color: var(--blue); line-height: 1; }
  .brand__mark { width: 12px; height: 12px; border-radius: 50%; background: var(--green-bright); }

  /* Right page */
  .mission-kicker { position: absolute; left: 63px; top: 38px; font-size: 16px; color: var(--blue); }
  .mission-title { position: absolute; left: 62px; top: 52px; font-size: 34px; font-weight: 700; line-height: 35px; color: var(--blue); }
  .intro { position: absolute; left: 63px; top: 162px; width: 180px; font-size: 23px; font-weight: 300; line-height: 25.5px; color: var(--blue); }
  .body-copy { position: absolute; font-size: 12px; line-height: 13.6px; color: var(--grey-text); }
  .body-copy--left { left: 63px; top: 428px; width: 184px; }
  .body-copy--right { left: 292px; top: 165px; width: 192px; }
  .photo { position: absolute; left: 292px; top: 346px; width: 196px; height: 257px;
    background: linear-gradient(180deg, #6a3a55 0%, #8a4a3a 30%, #4a2a2a 60%, #2a1a22 100%); }
</style>
</head>
<body>
  <main class="spread">
    <section class="page page--left">
      <p class="kicker">Lower energy cost</p>
      <h1 class="page-title">Success Stories</h1>
      <div class="rule" style="left:63px; top:138px; width:423px;"></div>

      <article class="stat" style="left:61px; top:181px;">
        <div class="stat__figure"><span class="stat__value stat__value--blue">$400,000</span></div>
        <p class="stat__text"><span class="stat__lead stat__lead--blue">3 year savings</span> for early learning centers by securing a low rate per kilowatt hour (kWh) for their electricity</p>
      </article>

      <article class="stat" style="left:309px; top:181px;">
        <div class="stat__figure">
          <svg class="donut" viewBox="0 0 46 46" aria-hidden="true"><circle cx="23" cy="23" r="17" fill="none" stroke="var(--ring-base)" stroke-width="8"/><circle cx="23" cy="23" r="17" fill="none" stroke="var(--green)" stroke-width="8" stroke-dasharray="53.4 106.8" transform="rotate(-90 23 23)"/></svg>
          <span class="stat__value stat__value--green">50%</span>
        </div>
        <p class="stat__text"><span class="stat__lead stat__lead--green">50% savings</span> for manufacturing firm by upgrading to LED lighting</p>
      </article>

      <article class="stat" style="left:61px; top:333px;">
        <div class="stat__figure">
          <svg class="donut" viewBox="0 0 46 46" aria-hidden="true"><circle cx="23" cy="23" r="17" fill="none" stroke="var(--ring-base)" stroke-width="8"/><circle cx="23" cy="23" r="17" fill="none" stroke="var(--green)" stroke-width="8" stroke-dasharray="28.8 106.8" transform="rotate(-90 23 23)"/></svg>
          <span class="stat__value stat__value--green">27%</span>
        </div>
        <p class="stat__text"><span class="stat__lead stat__lead--green">27% energy usage</span> reduction by implementing our Arc Series lighting controls for a Fortune 100 company</p>
      </article>

      <article class="stat" style="left:309px; top:333px;">
        <div class="stat__figure"><span class="stat__value stat__value--blue">$200,000</span></div>
        <p class="stat__text"><span class="stat__lead stat__lead--blue">Savings for</span> restaurant group on their electricity bills by competitive supplier bidding</p>
      </article>

      <article class="stat" style="left:61px; top:478px;">
        <div class="stat__figure">
          <svg class="donut" viewBox="0 0 46 46" aria-hidden="true"><circle cx="23" cy="23" r="17" fill="none" stroke="var(--ring-base)" stroke-width="8"/><circle cx="23" cy="23" r="17" fill="none" stroke="var(--green)" stroke-width="8" stroke-dasharray="32 106.8" transform="rotate(-90 23 23)"/></svg>
          <span class="stat__value stat__value--green">30%</span>
        </div>
        <p class="stat__text"><span class="stat__lead stat__lead--green">30% annual savings</span> for Distribution Center through lighting retrofit and HVAC controls</p>
      </article>

      <article class="stat" style="left:309px; top:478px;">
        <div class="stat__figure">
          <svg class="donut" viewBox="0 0 46 46" aria-hidden="true"><circle cx="23" cy="23" r="17" fill="none" stroke="var(--ring-base)" stroke-width="8"/><circle cx="23" cy="23" r="17" fill="none" stroke="var(--green)" stroke-width="8" stroke-dasharray="26.7 106.8" transform="rotate(-90 23 23)"/></svg>
          <span class="stat__value stat__value--green">25%</span>
        </div>
        <p class="stat__text"><span class="stat__lead stat__lead--green">25% reduction</span> in water usage for a property management company for their multi-unit buildings</p>
      </article>

      <div class="rule" style="left:63px; top:624px; width:423px;"></div>
      <div class="brand" style="left:61px;"><span class="brand__mark"></span>The Volt Group</div>
    </section>

    <div class="spine"></div>

    <section class="page page--right">
      <p class="mission-kicker">Our mission is simple:</p>
      <h2 class="mission-title">We help our clients<br>lower their energy costs</h2>
      <div class="rule" style="left:63px; top:137px; width:423px;"></div>

      <p class="intro">The Volt Group and its partner company, Lumen Energy Partners, are dedicated to helping you lower your company’s operating expenses.</p>

      <p class="body-copy body-copy--left">THE VOLT GROUP AND LEP are operating divisions of Summit Holding Corp, a publicly traded energy services company. As a vendor-independent company, there are many ways in which we help you lower your energy expenditures. The Volt Group (TVG) lowers the cost of energy through competitive supplier bidding and LEP creates comprehensive energy savings solutions through the implementation of energy reduction services.</p>

      <p class="body-copy body-copy--right">OUR DIVERSE PORTFOLIO of leading competitive energy suppliers, comprehensive energy efficiency solutions, best-in-class products, and unparalleled industry experience provide our clients with the confidence that they are getting the best solutions for their energy needs. BY REDUCING THE PRICE for energy and lowering usage, TVG and LEP allow businesses to keep more of their own capital.</p>

      <div class="photo" role="img" aria-label="Photograph of a city skyline at night with lit skyscrapers"></div>

      <div class="rule" style="left:63px; top:624px; width:423px;"></div>
      <div class="brand" style="right:62px;"><span class="brand__mark"></span>Lumen Energy Partners</div>
    </section>
  </main>
</body>
</html>
```